Diesel injection diagnostics and repairs

I am after a business card design for my business.
The business; repairs diesel fuel systems on 4wds, trucks, earthmoving equipment,can do mobile repairs and diagnostics
The business design can basic but effective, I guess some colours such as green and black or even blue......
The end result should reflect the business name and logo and what the business can do

Industry/Entity Type

Business

Contact Information for Business Card

BW Diesel Injection PTY LTD
bw_diesel@trovamail.net
Dennis Holt
0491570156

```html
<!DOCTYPE html>
<html lang="en">
<head>
<meta charset="utf-8">
<title>BW Diesel Injection – Business Card</title>
<link rel="stylesheet" href="https://fonts.googleapis.com/css2?family=Open+Sans:wght@400&display=swap">
<style>
  :root {
    --canvas-bg: #ffffff;
    --charcoal-top: #575757;
    --charcoal-bottom: #404040;
    --forest-green: #006837;
    --white: #ffffff;
  }
  html, body {
    margin: 0;
    padding: 0;
    width: 1200px;
    height: 1000px;
    overflow: hidden;
    background: var(--canvas-bg);
  }
  .card-sheet {
    display: block;
    width: 1200px;
    height: 1000px;
    font-family: "Open Sans", "Myriad Pro", sans-serif;
  }
  .stop-top { stop-color: var(--charcoal-top); }
  .stop-bottom { stop-color: var(--charcoal-bottom); }
  .band { fill: var(--forest-green); }
  .brand-dot { fill: var(--white); }
  .brand-name { fill: var(--white); font-size: 30px; }
  .brand-name-large { fill: var(--white); font-size: 36px; }
  .holder-name { fill: var(--white); font-size: 58px; }
  .holder-role { fill: var(--white); font-size: 32px; }
  .contact-line { fill: var(--white); font-size: 22px; }
</style>
</head>
<body>
<svg class="card-sheet" viewBox="0 0 1200 1000" xmlns="http://www.w3.org/2000/svg">
  <defs>
    <linearGradient id="card-face" x1="0" y1="0" x2="0" y2="1">
      <stop offset="0" class="stop-top"/>
      <stop offset="1" class="stop-bottom"/>
    </linearGradient>
  </defs>

  <g class="card card-front">
    <rect x="36" y="86" width="771" height="302" fill="url(#card-face)"/>
    <rect class="band" x="36" y="387" width="771" height="151"/>
    <path class="band" d="M352 388 Q352 363 380 363 L732 363 Q760 363 760 388 Z"/>

    <g class="brand-mark">
      <circle class="brand-dot" cx="120" cy="200" r="34"/>
      <text class="brand-name" x="170" y="211">BW Diesel</text>
    </g>

    <text class="holder-name" x="770" y="248" text-anchor="end">Dennis Holt</text>
    <text class="holder-role" x="752" y="290" text-anchor="end">manager</text>

    <text class="contact-line" x="726" y="405" text-anchor="end">BW Diesel Injection PTY LTD</text>
    <text class="contact-line" x="726" y="448" text-anchor="end">bw_diesel@trovamail.net</text>
    <text class="contact-line" x="726" y="490" text-anchor="end">Mobile: 0491570156</text>
  </g>

  <g class="card card-back">
    <rect class="band" x="807" y="461" width="358" height="41"/>
    <rect x="394" y="501" width="771" height="373" fill="url(#card-face)"/>
    <rect class="band" x="394" y="873" width="771" height="39"/>

    <g class="brand-mark">
      <circle class="brand-dot" cx="650" cy="687" r="42"/>
      <text class="brand-name-large" x="712" y="700">BW Diesel</text>
    </g>
  </g>
</svg>
</body>
</html>
```